Dalvor Inc Business Card

Looking to get an updated business card for a Contract Machining company (www.dalvorinc-example.com) - looking for a clean design the portrays the technical nature of the business - colors can follow the website design and be in any combination that makes sense (red black, white, metallic or silver) - logos attached for use also. Would like space for: Name, title, business phone (555 214-3098), cell phone , website (www.dalvorinc-example.com) - possibly QR code could be integrated for website (designer choice), business address - 418 Birchfield Lane, Alderton, MI 48790 (cards will be for 4 employees, I will either need to modify a template or I can provide individual information)
Target Market(s)
Aerospace, defense and medical device manufacturing companies that need machining
Industry/Entity Type
Machining for aerospace, defense, medical
Contact Information for Business Card
Name, Title, Business Phone, Cell Phone, email, business website and business address

```html
<!DOCTYPE html>
<html lang="en">
<head>
<meta charset="utf-8">
<title>Dalvor Inc Business Card</title>
<link rel="stylesheet" href="https://fonts.googleapis.com/css2?family=Poppins:wght@400;500;600;700&display=swap">
<style>
  :root {
    --stage: #2a2a2b;
    --card: #1c1d1f;
    --red: #b41f24;
    --white: #ffffff;
    --rule: #8a8a8a;
    --pattern-light: #8d8e90;
    --pattern-dark: #0c0c0d;
  }
  * { box-sizing: border-box; margin: 0; padding: 0; }
  html, body { width: 1200px; height: 1108px; overflow: hidden; }
  body {
    background: var(--stage);
    font-family: "Poppins", sans-serif;
    display: flex;
    align-items: center;
    justify-content: center;
    gap: 80px;
  }
  .card {
    width: 400px;
    height: 660px;
    border-radius: 22px;
    background: var(--card);
    position: relative;
    overflow: hidden;
    box-shadow: 0 18px 40px rgba(0,0,0,0.45);
  }
  .card-front {
    display: flex;
    flex-direction: column;
    align-items: center;
    padding-top: 62px;
    color: var(--white);
    text-align: center;
  }
  .brand-disc {
    width: 196px;
    height: 196px;
    border-radius: 50%;
    background: var(--red);
    flex: none;
  }
  .brand-name {
    margin-top: 14px;
    font-size: 42px;
    font-weight: 700;
    color: var(--red);
    letter-spacing: 1px;
    line-height: 1.1;
    white-space: nowrap;
  }
  .person-name {
    margin-top: 30px;
    font-size: 22px;
    font-weight: 600;
    color: var(--red);
    text-transform: uppercase;
    letter-spacing: 0.5px;
    line-height: 1.1;
  }
  .person-title {
    font-size: 18px;
    font-weight: 400;
    line-height: 1.3;
  }
  .icon-row {
    margin-top: 14px;
    width: 300px;
    display: flex;
    align-items: center;
    gap: 8px;
  }
  .icon-row .rule { flex: 1; height: 1px; background: var(--rule); }
  .icon-tile {
    width: 28px;
    height: 28px;
    border-radius: 4px;
    background: var(--red);
    display: flex;
    align-items: center;
    justify-content: center;
  }
  .contact-list {
    margin-top: 10px;
    list-style: none;
    font-size: 16px;
    line-height: 1.5;
  }
  .contact-list .accent { color: var(--red); }
  .address-rule {
    width: 300px;
    height: 1px;
    background: var(--rule);
    margin-top: 10px;
  }
  .address {
    margin-top: 8px;
    font-size: 16px;
    line-height: 1.45;
    font-style: normal;
  }
  .card-back .pattern-field {
    position: absolute;
    inset: 0;
    background: linear-gradient(225deg, var(--pattern-light) 0%, #3a3b3d 38%, #1a1b1c 65%, var(--pattern-dark) 100%);
  }
  .back-mark {
    position: absolute;
    left: 220px;
    top: 500px;
    display: flex;
    align-items: center;
    gap: 8px;
  }
  .back-mark .mark-disc {
    width: 40px;
    height: 40px;
    border-radius: 50%;
    background: var(--red);
  }
  .back-mark .mark-name {
    font-size: 14px;
    font-weight: 600;
    color: var(--white);
  }
</style>
</head>
<body>
  <section class="card card-front">
    <div class="brand-disc"></div>
    <div class="brand-name">DALVOR INC</div>
    <div class="person-name">Marcus Hale</div>
    <div class="person-title">Managing Director</div>
    <div class="icon-row">
      <span class="rule"></span>
      <span class="icon-tile" aria-label="Office phone">
        <svg width="18" height="18" viewBox="0 0 24 24"><path fill="#fff" d="M3 9c0-2 4-4 9-4s9 2 9 4v2h-5V9H8v2H3zM6 12h12l2 8H4z"/><circle cx="12" cy="16" r="2" fill="#b41f24"/></svg>
      </span>
      <span class="icon-tile" aria-label="Mobile phone">
        <svg width="18" height="18" viewBox="0 0 24 24"><rect x="7" y="2" width="10" height="20" rx="2" fill="none" stroke="#fff" stroke-width="2"/><circle cx="12" cy="18" r="1" fill="#fff"/></svg>
      </span>
      <span class="icon-tile" aria-label="Email">
        <svg width="18" height="18" viewBox="0 0 24 24"><rect x="2" y="5" width="20" height="14" fill="#fff"/><path d="M2 5l10 8 10-8" fill="none" stroke="#b41f24" stroke-width="1.6"/></svg>
      </span>
      <span class="icon-tile" aria-label="Website">
        <svg width="18" height="18" viewBox="0 0 24 24"><circle cx="12" cy="12" r="9" fill="#fff"/><path d="M3 12h18M12 3c3 3 3 15 0 18M12 3c-3 3-3 15 0 18" fill="none" stroke="#b41f24" stroke-width="1.4"/></svg>
      </span>
      <span class="rule"></span>
    </div>
    <ul class="contact-list">
      <li>555 214-3098</li>
      <li>555 386-7140</li>
      <li>info@dalvorinc-example.com</li>
      <li>www.<span class="accent">dalvorinc-example</span>.com</li>
    </ul>
    <div class="address-rule"></div>
    <address class="address">418 Birchfield Lane,<br>Alderton, MI 48790</address>
  </section>

  <section class="card card-back">
    <div class="pattern-field" role="img" aria-label="Repeating grid of company emblems in glossy black, fading to silver toward the top corner"></div>
    <div class="back-mark">
      <span class="mark-disc"></span>
      <span class="mark-name">Dalvor Inc</span>
    </div>
  </section>
</body>
</html>
```